Business Stationary, Letterhead, Fax Cover Sheet, Client Intake, Email Signature, Thank you cards.
Marwick Law Firm
Business Stationary, Letterhead, Fax Cover Sheet, Client Intake, Email Signature, Thank you cards. - Law
Creative Brief
Professional
Len Marwick
Lawyer
2837 Falbrook St., Suite 1940 Houston, Texas 77014
len@marwick-law.example
www.marwick-law.example
Please note this project is Not for just One Person but for All Staff. The files should be in editable format to allow for different names and titles on cards.

```html
<!DOCTYPE html>
<html lang="en">
<head>
<meta charset="utf-8">
<title>Marwick Law Firm – Business Cards</title>
<link href="https://fonts.googleapis.com/css2?family=Tinos:wght@400;700&display=swap" rel="stylesheet">
<style>
  :root {
    --backdrop: #5f5a52;
    --card-black: #060606;
    --card-white: #f2f2f2;
    --ink-light: #f4f4f4;
    --ink-dark: #3a3a3a;
    --brand-blue: #2f9be0;
    --rule-blue: #1d86d6;
    --shadow: rgba(0, 0, 0, 0.45);
  }
  * { box-sizing: border-box; margin: 0; padding: 0; }
  html, body { width: 1200px; height: 906px; overflow: hidden; }
  body {
    background: var(--backdrop);
    font-family: "Tinos", "Times New Roman", serif;
    position: relative;
  }
  .card {
    position: absolute;
    border-radius: 48px;
    overflow: hidden;
    background: var(--card-black);
    color: var(--ink-light);
    box-shadow: 0 6px 16px var(--shadow);
  }
  .card--vertical { left: 86px; top: 73px; width: 379px; height: 735px; }
  .card--horizontal { left: 502px; top: 73px; width: 661px; height: 395px; }
  .card--split { left: 502px; top: 494px; width: 661px; height: 363px; }

  .brand {
    position: absolute;
    display: flex;
    align-items: center;
    justify-content: center;
    gap: 12px;
    font-size: 24px;
    line-height: 28px;
    font-weight: 700;
    letter-spacing: 0.06em;
    color: var(--brand-blue);
    text-transform: uppercase;
  }
  .brand__dot {
    width: 14px; height: 14px;
    border-radius: 50%;
    background: var(--brand-blue);
    flex: none;
  }
  .brand__name { display: flex; flex-direction: column; white-space: nowrap; }

  .details { position: absolute; font-size: 17px; line-height: 25px; }
  .details__name {
    font-variant: small-caps;
    font-size: 29px;
    line-height: 30px;
    letter-spacing: 0.02em;
  }
  .details__title { font-size: 20px; line-height: 26px; margin-bottom: 24px; }
  .details__group { margin-bottom: 12px; }
  .details__group:last-child { margin-bottom: 0; }

  /* vertical card */
  .card--vertical .brand { left: 0; right: 0; top: 168px; font-size: 26px; line-height: 31px; }
  .card--vertical .rule {
    position: absolute; left: 40px; right: 40px; top: 268px; height: 2px;
    background: linear-gradient(90deg, transparent, var(--rule-blue) 25%, var(--rule-blue) 75%, transparent);
  }
  .card--vertical .details { left: 0; right: 0; top: 300px; text-align: center; }

  /* horizontal card */
  .card--horizontal .brand { left: 0; width: 290px; top: 168px; }
  .card--horizontal .rule {
    position: absolute; left: 290px; top: 35px; width: 2px; height: 320px;
    background: linear-gradient(180deg, transparent, var(--rule-blue) 20%, var(--rule-blue) 80%, transparent);
  }
  .card--horizontal .details { right: 48px; top: 40px; text-align: right; }

  /* split card */
  .card--split .panel-light {
    position: absolute; left: 306px; top: 0; right: 0; bottom: 0;
    background: var(--card-white);
  }
  .card--split .brand { left: 0; width: 306px; top: 160px; }
  .card--split .details { right: 40px; top: 42px; text-align: right; color: var(--ink-dark); }
  .card--split .details__name { color: var(--brand-blue); }
</style>
</head>
<body>

  <section class="card card--vertical" aria-label="Vertical business card">
    <div class="brand"><span class="brand__dot"></span><span class="brand__name"><span>Marwick</span><span>Law Firm</span></span></div>
    <div class="rule"></div>
    <div class="details">
      <p class="details__name">Len Marwick</p>
      <p class="details__title">Lawyer</p>
      <div class="details__group"><p>Phone: 713-555-0148</p><p>Fax: 713-555-0149</p></div>
      <div class="details__group"><p>2837 Falbrook St., Suite 1940</p><p>Houston, Texas 77014</p></div>
      <div class="details__group"><p>len@marwick-law.example</p><p>www.marwick-law.example</p></div>
    </div>
  </section>

  <section class="card card--horizontal" aria-label="Horizontal business card">
    <div class="brand"><span class="brand__dot"></span><span class="brand__name"><span>Marwick</span><span>Law Firm</span></span></div>
    <div class="rule"></div>
    <div class="details">
      <p class="details__name">Len Marwick</p>
      <p class="details__title">Lawyer</p>
      <div class="details__group"><p>Phone: 713-555-0148</p><p>Fax: 713-555-0149</p></div>
      <div class="details__group"><p>2837 Falbrook St., Suite 1940</p><p>Houston, Texas 77014</p></div>
      <div class="details__group"><p>len@marwick-law.example</p><p>www.marwick-law.example</p></div>
    </div>
  </section>

  <section class="card card--split" aria-label="Two-tone business card">
    <div class="panel-light"></div>
    <div class="brand"><span class="brand__dot"></span><span class="brand__name"><span>Marwick</span><span>Law Firm</span></span></div>
    <div class="details">
      <p class="details__name">Len Marwick</p>
      <p class="details__title">Lawyer</p>
      <div class="details__group"><p>Phone: 713-555-0148</p><p>Fax: 713-555-0149</p></div>
      <div class="details__group"><p>2837 Falbrook St., Suite 1940</p><p>Houston, Texas 77014</p></div>
      <div class="details__group"><p>len@marwick-law.example</p><p>www.marwick-law.example</p></div>
    </div>
  </section>

</body>
</html>
```